Name card design for KORU mobile accessories company

KORU is an upmarket brand, we are looking for professional business card design.

the design should be neat and simple but giving a strong feeling.
should not be colorful. make it black/white/gray tone

Name:
Job title:
Contact no.:
company address: i would like the company address to be very small and thin.
link to social media profile:
company website:

*the company have no website yet
as the project is done please i also would like the font that use in design as well; for more further people in company need a business card:)
Updates

Thank you for all super fast submission :D they're all look cool!

i have just update my brief to make the statement clearer, please check it out :)
if you have any question please dont hesitate to ask.
i would like see more design from you! 
Keep it up!  :D

Target Market(s)

Company target are upmarket company distributor, such as Velmora and Quill store.

Industry/Entity Type

Business

Font styles to use
Serif
Sans Serif
Other font styles liked:
• Formal and mordern

Colors
ffffff
eeeeee
d3d3d3
919191
474747
1b1b1b
000000
333333

Requirements
Must have
• The design must be professional clean and clear but also Strong and Modern!
text should be formal and mordern
Should not have
• No complicated design!

```html
<!DOCTYPE html>
<html lang="en">
<head>
<meta charset="utf-8">
<title>KORU Business Card</title>
<link rel="stylesheet" href="https://fonts.googleapis.com/css2?family=Open+Sans:wght@300;400;600;700;800&display=swap">
<style>
  :root {
    --white: #ffffff;
    --paper: #f4f4f4;
    --pattern: #eeeeee;
    --light-gray: #d3d3d3;
    --mid-gray: #919191;
    --dark-gray: #474747;
    --ink: #1b1b1b;
    --black: #000000;
  }
  * { margin: 0; padding: 0; box-sizing: border-box; }
  html, body {
    width: 1200px; height: 846px; overflow: hidden;
    background: var(--black);
    font-family: "Open Sans", Arial, sans-serif;
  }
  .stage { position: relative; width: 1200px; height: 846px; }

  /* Front card */
  .card-front {
    position: absolute; left: 40px; top: 40px;
    width: 660px; height: 384px;
    background: var(--white);
    overflow: hidden;
  }
  .brand-pattern {
    position: absolute; left: 0; top: 0; right: 0; bottom: 60px;
    background: linear-gradient(135deg, var(--paper), var(--pattern));
  }
  .brand-name {
    position: absolute; right: 44px; top: 52px;
    font-weight: 800; font-size: 78px; line-height: 1;
    letter-spacing: 2px; color: var(--ink);
  }
  .holder { position: absolute; left: 78px; top: 168px; }
  .holder-name {
    font-weight: 700; font-size: 20px; line-height: 24px; color: var(--ink);
    letter-spacing: 0.3px; text-transform: uppercase;
  }
  .holder-title {
    font-size: 15px; line-height: 18px; color: var(--mid-gray);
    text-transform: uppercase;
  }
  .contact-list {
    position: absolute; left: 78px; top: 232px;
    list-style: none; font-size: 14px; line-height: 19px; color: var(--ink);
  }
  .contact-list .address {
    font-weight: 300; font-size: 12px; color: var(--dark-gray);
  }
  .footer {
    position: absolute; left: 0; right: 0; bottom: 0; height: 60px;
    display: flex;
  }
  .footer-band {
    flex: 0 0 400px; background: var(--ink);
    display: flex; align-items: center; justify-content: flex-end;
    padding-right: 22px;
  }
  .footer-accent { flex: 1; background: var(--mid-gray); }
  .website {
    color: var(--white); font-weight: 600; font-size: 16px;
    letter-spacing: 5px;
  }

  /* Back card */
  .card-back {
    position: absolute; left: 500px; top: 446px;
    width: 660px; height: 384px;
    background: var(--black);
    border: 1px solid var(--white);
    display: flex; align-items: center; justify-content: center;
  }
  .brand-name-large {
    font-weight: 800; font-size: 120px; line-height: 1;
    letter-spacing: 6px; color: var(--white);
  }
</style>
</head>
<body>
<main class="stage">
  <section class="card-front">
    <div class="brand-pattern" role="img" aria-label="Faint repeating brand-mark pattern across the card face"></div>
    <div class="brand-name">KORU</div>
    <div class="holder">
      <p class="holder-name">Tobin R. Aswell</p>
      <p class="holder-title">Director</p>
    </div>
    <ul class="contact-list">
      <li>T:00000000000</li>
      <li>M:000000000</li>
      <li class="address">Adress:00000000000</li>
      <li>E:info@koru.com</li>
    </ul>
    <div class="footer">
      <div class="footer-band"><p class="website">www.koru.com</p></div>
      <div class="footer-accent"></div>
    </div>
  </section>

  <section class="card-back">
    <span class="brand-name-large">KORU</span>
  </section>
</main>
</body>
</html>
```